Anzeigengestaltung für Steuerberatung
Zielgruppe
Steuerberatung, Zielgruppe: Unternehmen und Privatpersonen
Aufgabenstellung
Logo, Anschrift mit vollständigem Namen, Stichwörter: nahbar.ehrlich.weise begleitet.
Farbe wie Logo auf der Website. Anbei die Farbcodes C32 M38 Y37 K15
Anzeige soll frisch, ansprechend, jung, klare Informationen ohne verspielte Details. Trotzdem im Stil des bisherigen bewegen.
Anzeigengröße: 9,00 x 6,50 cm

```html
<!DOCTYPE html>
<html lang="de">
<head>
<meta charset="utf-8">
<title>Miriam Kohl Steuerberatung – Anzeige</title>
<link rel="stylesheet" href="https://fonts.googleapis.com/css2?family=Barlow:wght@300;400;500&display=swap">
<style>
  :root {
    --stage: #222f3d;
    --taupe: #a48a81;
    --taupe-dark: #6f5951;
    --brand-text: #8a726a;
    --paper: #ffffff;
    --badge: #98d23c;
    --photo-wall: #8d8a88;
    --photo-jacket: #d9c9b8;
    --photo-wood: #a37c5a;
  }
  * { margin: 0; padding: 0; box-sizing: border-box; }
  html, body { width: 1200px; height: 1012px; overflow: hidden; }
  body {
    background: var(--stage);
    font-family: "Barlow", Arial, sans-serif;
    position: relative;
  }
  .ad {
    position: absolute;
    left: 100px; top: 145px;
    width: 1000px; height: 722px;
    background: var(--taupe);
    overflow: hidden;
  }
  .ad-shapes { position: absolute; inset: 0; }
  .brand {
    position: absolute;
    left: 120px; top: 130px;
    display: flex;
    align-items: center;
    gap: 18px;
    color: var(--brand-text);
  }
  .brand-dot {
    flex: none;
    width: 52px; height: 52px;
    border-radius: 50%;
    background: var(--brand-text);
  }
  .brand-name {
    font-size: 30px;
    font-weight: 400;
    line-height: 1.2;
  }
  .headline {
    position: absolute; left: 0; top: 0;
    color: var(--paper);
    font-weight: 500;
    font-size: 56px;
    line-height: 1;
    text-transform: uppercase;
  }
  .headline span { position: absolute; white-space: nowrap; }
  .headline .l1 { left: 55px; top: 322px; }
  .headline .l2 { left: 181px; top: 381px; }
  .headline .l3 { left: 113px; top: 441px; }
  .contact-rule {
    position: absolute; left: 39px; top: 508px;
    width: 2px; height: 214px; background: var(--paper);
  }
  .contact {
    position: absolute; left: 73px; top: 546px;
    color: var(--paper);
    font-size: 31px;
    line-height: 38px;
    list-style: none;
  }
  .contact .strong { font-weight: 500; }
  .contact .light { font-weight: 300; }
</style>
</head>
<body>
  <section class="ad">
    <svg class="ad-shapes" width="1000" height="722" viewBox="0 0 1000 722">
      <defs>
        <linearGradient id="photoTone" x1="0" y1="0" x2="0.3" y2="1">
          <stop offset="0" stop-color="var(--photo-wall)"/>
          <stop offset="0.45" stop-color="var(--photo-jacket)"/>
          <stop offset="1" stop-color="var(--photo-wood)"/>
        </linearGradient>
      </defs>
      <polygon class="panel-shadow" points="0,0 97,296 92,305 0,14" fill="var(--taupe-dark)"/>
      <polygon class="panel-white" points="0,0 758,0 682,226 97,296" fill="var(--paper)"/>
      <polygon class="photo" points="758,0 1000,0 1000,722 522,722" fill="url(#photoTone)"
               role="img" aria-label="Foto der Steuerberaterin, sitzend in heller Jacke im Büro"/>
      <rect class="badge" x="686" y="565" width="110" height="106" rx="8" fill="var(--badge)"
            role="img" aria-label="Zertifikatssiegel 2024"/>
      <rect class="badge" x="827" y="563" width="110" height="106" rx="8" fill="var(--badge)"
            role="img" aria-label="Zertifikatssiegel 2025"/>
    </svg>

    <div class="brand">
      <span class="brand-dot"></span>
      <div class="brand-name">Miriam Kohl<br>Steuerberatung</div>
    </div>

    <h1 class="headline">
      <span class="l1">Nahbar</span>
      <span class="l2">Weise begleitet</span>
      <span class="l3">Ehrlich</span>
    </h1>

    <div class="contact-rule"></div>
    <ul class="contact">
      <li class="strong">07123/4567890</li>
      <li class="light">Lindenweg 12</li>
      <li class="light">72000 Musterstadt</li>
      <li class="strong">kohl-steuerberatung.de</li>
    </ul>
  </section>
</body>
</html>
```